Bright Ember Publicity is a new boutique Press Office with a small roster of well-chosen clients across an array of disciplines; from Art and Technology to Restaurants and Fashion. Based in Greenpoint Brooklyn, Bright Ember Publicity achieves outstanding results through hard work, tenacity, efficiency and a sense of humor. We need a simple, versatile and classic design. We would like each side of the card to be white text on a black background.

Boutique

```html
<!DOCTYPE html>
<html lang="en">
<head>
<meta charset="utf-8">
<title>Bright Ember Publicity – Business Card</title>
<link href="https://fonts.googleapis.com/css2?family=Cinzel:wght@500&family=Montserrat:wght@400;600&display=swap" rel="stylesheet">
<style>
  :root {
    --backdrop: #d6d6d6;
    --card: #111111;
    --ink: #ffffff;
    --muted: #dcdcdc;
    --ghost: #262626;
    --rule: #ffffff;
  }
  * { box-sizing: border-box; margin: 0; padding: 0; }
  html, body { width: 1200px; height: 900px; overflow: hidden; }
  body { background: var(--backdrop); position: relative; font-family: "Montserrat", sans-serif; color: var(--ink); }

  .card {
    position: absolute;
    width: 525px;
    height: 300px;
    background: var(--card);
    border-radius: 22px;
    overflow: hidden;
    box-shadow: 0 14px 30px rgba(0,0,0,.35);
  }
  .card--front { left: 80px; top: 120px; }
  .card--back  { left: 595px; top: 480px; }

  /* Front */
  .front-name {
    position: absolute; left: 0; right: 0; top: 88px;
    text-align: center;
    font-family: "Cinzel", serif; font-weight: 500;
    font-size: 40px; line-height: 1.15; letter-spacing: 2px;
  }
  .front-web {
    position: absolute; left: 0; right: 0; bottom: 34px;
    text-align: center; font-weight: 600; font-size: 17px; letter-spacing: .3px;
  }

  /* Back */
  .ghost-name {
    position: absolute; right: 22px; top: 0; height: 300px;
    writing-mode: vertical-rl;
    display: flex; justify-content: center;
    font-family: "Cinzel", serif; font-weight: 500;
    font-size: 70px; line-height: 1; color: var(--ghost);
  }
  .brand {
    position: absolute; left: 30px; top: 46px;
    font-family: "Cinzel", serif; font-weight: 500;
    font-size: 25px; line-height: 1.2; letter-spacing: 2.5px;
  }
  .divider {
    position: absolute; left: 0; right: 0; top: 138px;
    border-top: 1.5px solid var(--rule);
  }
  .person__name {
    position: absolute; right: 112px; top: 108px;
    font-family: "Cinzel", serif; font-weight: 500; font-size: 20px; letter-spacing: 1px;
  }
  .person__role {
    position: absolute; right: 112px; top: 147px;
    font-size: 12px; color: var(--muted);
  }

  .contact { position: absolute; left: 30px; top: 152px; font-size: 14px; line-height: 21px; color: var(--muted); }
  .contact__list { list-style: none; margin-top: 2px; }
  .contact__list li { display: flex; align-items: center; gap: 10px; }
  .contact__list svg { width: 12px; height: 12px; fill: none; stroke: var(--muted); stroke-width: 1.6; }
</style>
</head>
<body>
  <section class="card card--front" aria-label="Card front">
    <div class="front-name">Bright Ember<br>Publicity</div>
    <div class="front-web">www.brightember.com</div>
  </section>

  <section class="card card--back" aria-label="Card back">
    <div class="ghost-name" aria-hidden="true">Ember</div>
    <div class="brand">Bright Ember<br>Publicity</div>
    <div class="person__name">Marla Quinn</div>
    <div class="divider"></div>
    <div class="person__role">Director</div>
    <div class="contact">
      <p>418 Franklin St #2B</p>
      <p>Brooklyn, NY 11222</p>
      <ul class="contact__list">
        <li><svg viewBox="0 0 12 12"><rect x="3" y="1" width="6" height="10" rx="1"/></svg>+330 2460-7315</li>
        <li><svg viewBox="0 0 12 12"><path d="M1 4c2-3 8-3 10 0M3 5h6l1 5H2z"/></svg>+330 2360-4198</li>
        <li><svg viewBox="0 0 12 12"><rect x="1" y="2.5" width="10" height="7"/><path d="M1 2.5l5 4 5-4"/></svg>info@brightember.com</li>
        <li><svg viewBox="0 0 12 12"><circle cx="6" cy="6" r="5"/><path d="M1 6h10M6 1c-2.5 3-2.5 7 0 10M6 1c2.5 3 2.5 7 0 10"/></svg>www.brightember.com</li>
      </ul>
    </div>
  </section>
</body>
</html>
```